A Lowen Grad

This poster is to show how we want the world to view our high school students when the graduate. The values and lessons they should live by.
I'd like for the middle to say "A LOWEN GRAD IS..." and it should be surrounded by the following values:
Never Quits
Doesn't Put Others Down
Respects Everyone
Learns from their mistakes
Takes action
Always looks to Improve
Looks to the future
Puts others' needs before our own

and the final emotion one should have more emphasis....
will always be a part of Lowen

I want it to look cool and sleek, not just listed out. Maybe a thought bubble or something like that. Please use school colors and use the school logo

```html
<!DOCTYPE html>
<html lang="en">
<head>
<meta charset="utf-8">
<title>A Lowen Grad</title>
<link href="https://fonts.googleapis.com/css2?family=Montserrat:wght@900&family=Architects+Daughter&display=swap" rel="stylesheet">
<style>
  :root {
    --backdrop: #e8e5e0;
    --board-light: #4a7d5a;
    --board-dark: #2f5e40;
    --chalk: #ffffff;
    --chalk-haze: rgba(255,255,255,0.14);
    --ledge: #b0623a;
    --ledge-dark: #8a4426;
    --eraser: #3a0f16;
    --paper: #ffffff;
    --navy: #23205a;
    --gold: #d9ac2a;
    --photo-light: #bdbdbd;
    --photo-dark: #1c1c1c;
  }
  html, body {
    margin: 0;
    padding: 0;
    width: 939px;
    height: 1200px;
    overflow: hidden;
    background: var(--backdrop);
  }
  .poster {
    position: absolute;
    left: 59px;
    top: 20px;
    width: 820px;
    height: 1159px;
    background: var(--paper);
    box-shadow: 0 4px 18px rgba(0,0,0,0.18);
  }
  .chalkboard {
    position: absolute;
    left: 0;
    top: 0;
    width: 820px;
    height: 645px;
    display: block;
  }
  .headline {
    font-family: "Montserrat", sans-serif;
    font-weight: 900;
    fill: var(--chalk);
    letter-spacing: -0.5px;
  }
  .value-text {
    font-family: "Architects Daughter", cursive;
    fill: var(--chalk);
    font-size: 16px;
    letter-spacing: 1.2px;
  }
  .value-box, .connector {
    fill: none;
    stroke: var(--chalk);
    stroke-width: 2;
    stroke-linecap: round;
    stroke-linejoin: round;
  }
  .sketch-area {
    fill: var(--chalk-haze);
  }
  .school-mark {
    position: absolute;
    left: 0;
    top: 770px;
    width: 820px;
    text-align: center;
  }
  .school-mark__dot {
    display: block;
    width: 96px;
    height: 96px;
    margin: 0 auto 14px;
    border-radius: 50%;
    background: var(--gold);
  }
  .school-mark__name {
    font-family: "Montserrat", sans-serif;
    font-weight: 900;
    font-size: 30px;
    letter-spacing: 3px;
    color: var(--navy);
  }
  .class-photo {
    position: absolute;
    left: 84px;
    top: 996px;
    width: 652px;
    height: 163px;
    border-radius: 120px 120px 0 0;
    background: linear-gradient(180deg, var(--photo-light) 0%, #555 35%, var(--photo-dark) 100%);
  }
</style>
</head>
<body>
<main class="poster">
  <svg class="chalkboard" viewBox="0 0 820 645" xmlns="http://www.w3.org/2000/svg" role="img" aria-label="Chalkboard with the values of a Lowen graduate joined by arrows">
    <defs>
      <linearGradient id="boardTone" x1="0" y1="0" x2="0" y2="1">
        <stop offset="0" stop-color="#2f5e40"/>
        <stop offset="0.5" stop-color="#4a7d5a"/>
        <stop offset="1" stop-color="#2f5e40"/>
      </linearGradient>
      <marker id="arrowHead" viewBox="0 0 10 10" refX="8" refY="5" markerWidth="7" markerHeight="7" orient="auto-start-reverse">
        <path d="M1 1 L9 5 L1 9 Z" fill="none" stroke="#fff" stroke-width="1.4"/>
      </marker>
    </defs>

    <rect class="board-surface" x="0" y="0" width="820" height="621" fill="url(#boardTone)"/>
    <rect class="board-ledge" x="0" y="621" width="820" height="24" fill="var(--ledge)"/>
    <rect class="board-ledge-edge" x="0" y="638" width="820" height="7" fill="var(--ledge-dark)"/>
    <rect class="chalk-stick" x="77" y="607" width="88" height="12" rx="3" fill="#f2f2f2"/>
    <rect class="chalk-stick" x="230" y="608" width="66" height="11" rx="3" fill="#f2f2f2"/>
    <rect class="board-eraser" x="525" y="574" width="203" height="46" rx="3" fill="var(--eraser)"/>

    <text class="headline" x="270" y="102" font-size="27">A LOWEN GRAD IS...</text>

    <path class="connector" d="M269 99 L259 99 L243 122" marker-end="url(#arrowHead)"/>
    <path class="connector" d="M250 176 L250 189 L330 183" marker-end="url(#arrowHead)"/>
    <path class="connector" d="M467 157 L499 154" marker-end="url(#arrowHead)"/>
    <path class="connector" d="M575 183 L570 258" marker-end="url(#arrowHead)"/>
    <path class="connector" d="M394 285 L290 269" marker-end="url(#arrowHead)"/>
    <path class="connector" d="M196 289 L203 400" marker-end="url(#arrowHead)"/>
    <path class="connector" d="M304 420 L346 405" marker-end="url(#arrowHead)"/>
    <path class="connector" d="M539 388 L575 402" marker-end="url(#arrowHead)"/>
    <path class="connector" d="M625 452 L595 480" marker-end="url(#arrowHead)"/>

    <g transform="rotate(-6 238 150)">
      <rect class="value-box" x="152" y="126" width="172" height="48" rx="10"/>
      <text class="value-text" x="238" y="157" text-anchor="middle" font-size="18">NEVER QUITS</text>
    </g>

    <rect class="value-box" x="341" y="148" width="126" height="108" rx="10"/>
    <text class="value-text" x="404" y="177" text-anchor="middle">DOESN'T</text>
    <text class="value-text" x="404" y="197" text-anchor="middle">PUT</text>
    <text class="value-text" x="404" y="217" text-anchor="middle">OTHERS</text>
    <text class="value-text" x="404" y="237" text-anchor="middle">DOWN</text>

    <rect class="value-box" x="504" y="135" width="178" height="46" rx="12"/>
    <text class="value-text" x="593" y="164" text-anchor="middle">TAKES ACTION</text>

    <g transform="rotate(-3 194 258)">
      <rect class="value-box" x="105" y="228" width="178" height="60" rx="14"/>
      <text class="value-text" x="194" y="254" text-anchor="middle" font-size="15">ALWAYS LOOKS</text>
      <text class="value-text" x="200" y="275" text-anchor="middle" font-size="15">TO IMPROVE</text>
    </g>

    <g transform="rotate(-5 540 303)">
      <rect class="value-box" x="388" y="272" width="304" height="64" rx="28"/>
      <text class="value-text" x="540" y="313" text-anchor="middle" font-size="23">RESPECTS  EVERYONE</text>
    </g>

    <rect class="sketch-area" x="240" y="296" width="86" height="84" rx="42" role="img" aria-label="Chalk sketch of a small chart"/>
    <rect class="sketch-area" x="596" y="188" width="124" height="56" rx="10" role="img" aria-label="Chalk sketch of linked dots"/>

    <rect class="value-box" x="347" y="366" width="192" height="62" rx="10"/>
    <text class="value-text" x="443" y="392" text-anchor="middle" font-size="18">LOOKS TO THE</text>
    <text class="value-text" x="460" y="414" text-anchor="middle" font-size="18">FUTURE</text>

    <rect class="value-box" x="146" y="402" width="160" height="56" rx="26"/>
    <text class="value-text" x="224" y="426" text-anchor="middle" font-size="14">LEARNS FROM</text>
    <text class="value-text" x="226" y="447" text-anchor="middle" font-size="14">THEIR MISTAKES</text>

    <rect class="value-box" x="560" y="396" width="160" height="56" rx="26"/>
    <text class="value-text" x="640" y="419" text-anchor="middle" font-size="14">PUTS OTHERS'</text>
    <text class="value-text" x="640" y="440" text-anchor="middle" font-size="14">NEEDS BEFORE</text>

    <text class="headline" x="410" y="515" font-size="31" text-anchor="middle">WILL ALWAYS BE A PART OF</text>
  </svg>

  <div class="school-mark">
    <span class="school-mark__dot"></span>
    <span class="school-mark__name">LOWEN ACADEMY</span>
  </div>

  <div class="class-photo" role="img" aria-label="Black and white group photo of the graduating class"></div>
</main>
</body>
</html>
```